Web Design for historic veg friendly, organic restaurant

We need a new web site. The Millbrook Cafe is a 40 year old restaurant in Chicago. We've been one of the premier, casual vegetarian restaurants since we opened. 5 years ago, Millbrook Cafe was purchased from the original owners by a local, certified organic farmer. We are nearly 100% from scratch kitchen, 100% certified organic produce, we are governed by a strict sustainable plan and we are very active politically. But you wouldn't know it form our website! We have a desire to build a simple website around some basic principles:
1. We need our current logo prominently displayed (logo attached)
2. We need a "click to call" easily accessible
3. We have an online order link that needs to be easily accessible
4. We need our hours, location, and directions easy to see
4. We need a separate events page (we have a live music and events venue that runs shows 5-7 nights per week.)
5. We would like to have a separate page for pictures, particularly old pictures. It would be fun to have a function for people to post their own shots, but that might make this too complicated. If it were possible, we would of course need to retain the ability to curate posted pictures.
6. This needs to be easily edited by us, so in a platform such as word press or similar
7. We will need this mobile enhanced

Target Market(s)

Neighborhood residents - zip code is 48213

Industry/Entity Type

Restaurant

Coding

Coded - Design and coding required

Number of Pages Required

4 page

Font styles to use
Sans Serif

Requirements
Must have
• Logo, click to call, events page that we can manage, contact us, about us page, menu (we have the online menu through a third party plugin), a page for our market and some nice pictures on our splash page,
• Must be mobile ready and on a platform such as Word Press or some other platform where we can edit on our own
Nice to have
• Page for past employees and historical pictures, be nice to have food pictures or something similar on a scroll, would love to have an ability for others to post pictures that we would "approve"
Should not have
• We don't need anything that spins, moves, flames or other features that detract from gathering information

```html
<!DOCTYPE html>
<html lang="en">
<head>
<meta charset="utf-8">
<title>Millbrook Cafe</title>
<link rel="stylesheet" href="https://fonts.googleapis.com/css2?family=Nunito:wght@400;600;700&display=swap">
<style>
:root{
  --black:#0b0b0b;
  --yellow:#f5d92f;
  --yellow-dark:#d8bb12;
  --red:#d71920;
  --wood:#5b3520;
  --wood-dark:#3a2012;
  --pink:#d9818a;
  --lilac:#c9b2d4;
  --text:#222;
  --muted:#8a8a8a;
  --white:#fff;
}
*{box-sizing:border-box;margin:0;padding:0}
html,body{width:1200px;height:2765px;overflow:hidden;background:var(--white)}
body{font-family:'Nunito',sans-serif;color:var(--text);position:relative}
h1,h2,h3,h4{font-weight:400}
.abs{position:absolute}

/* top bar */
.topbar{position:absolute;left:0;top:0;width:1200px;height:105px;background:var(--black)}
.pill{position:absolute;top:40px;height:47px;border-radius:24px;font-size:17px;font-weight:600;display:flex;align-items:center;justify-content:center}
.pill-pickup{left:576px;width:161px;background:var(--yellow);color:var(--black)}
.pill-delivery{left:746px;width:161px;background:var(--red);color:var(--white)}
.call{position:absolute;left:938px;top:24px;color:var(--white)}
.call-label{font-size:15px;display:flex;align-items:center;gap:5px;padding-left:16px}
.call-number{font-size:23px;font-weight:600;margin-top:4px;letter-spacing:.5px}

/* nav */
.mainnav{position:absolute;left:0;top:105px;width:1200px;height:57px;background:var(--yellow);border-bottom:2px solid var(--yellow-dark);display:flex;justify-content:center}
.mainnav a{display:flex;align-items:center;padding:0 24px;font-size:15px;font-weight:600;color:var(--black);text-decoration:none;border-right:1px solid var(--yellow-dark)}
.mainnav a:last-child{border-right:none}

/* hero */
.hero{position:absolute;left:0;top:162px;width:1200px;height:600px;overflow:hidden}
.hero-bg{position:absolute;inset:0;background:linear-gradient(100deg,var(--wood-dark),var(--wood) 40%,#6d4127 60%,var(--wood-dark))}
.brand{position:absolute;left:0;width:1200px;top:150px;display:flex;justify-content:center;align-items:center;gap:22px}
.brand-dot{width:44px;height:44px;border-radius:50%;background:var(--yellow)}
.brand-name{font-size:92px;font-weight:700;color:var(--yellow);line-height:1}
.hero-kicker{position:absolute;top:340px;width:1200px;text-align:center;color:var(--white);font-size:35px;font-weight:400}
.hero-title{position:absolute;top:380px;width:1200px;text-align:center;color:var(--white);font-size:45px;font-weight:600;line-height:1.12}
.arrow{position:absolute;top:226px;width:50px;height:50px;border:2px solid var(--white);border-radius:50%;display:flex;align-items:center;justify-content:center}
.arrow-prev{left:99px}.arrow-next{left:1049px}

/* welcome */
.welcome-title{position:absolute;top:805px;width:1200px;text-align:center;font-size:39px}
.welcome-title span{color:var(--red)}
.welcome-text{position:absolute;top:878px;left:262px;width:676px;text-align:center;color:var(--muted);font-size:17px;line-height:29px}
.btn-dark{position:absolute;left:516px;top:1032px;width:164px;height:44px;border-radius:22px;background:var(--black);color:var(--white);font-size:17px;display:flex;align-items:center;justify-content:center}

/* features */
.features{position:absolute;left:0;top:1163px;width:1200px;height:468px;background:linear-gradient(90deg,var(--lilac),var(--pink) 30%,#cf8f9c 50%,var(--pink) 70%,var(--lilac))}
.badge{position:absolute;top:118px;width:288px;height:288px;border-radius:50%;border:4px solid var(--white);background:radial-gradient(circle,#3a3232,#1a1414);display:flex;flex-direction:column;align-items:center;justify-content:flex-end;padding-bottom:70px;color:var(--white);font-size:27px;font-weight:700;outline:2px solid var(--white);outline-offset:6px}
.badge .bar{width:22px;height:4px;background:var(--white);margin-top:8px;border-radius:2px}
.badge-menu{left:129px}.badge-music{left:449px;background:radial-gradient(circle,#4a2a45,#1c1020)}.badge-farm{left:768px;background:radial-gradient(circle,#5b5a3a,#262614)}

/* events */
.events-title{position:absolute;top:1668px;width:1200px;text-align:center;font-size:38px;color:var(--red)}
.event{position:absolute;top:1747px;width:304px;text-align:center}
.event-photo{width:304px;height:227px}
.event-name{font-size:25px;margin-top:16px}
.event-rule{width:52px;height:3px;background:var(--red);margin:4px auto 10px}
.event-text{font-size:13px;color:#666;line-height:19px;padding:0 14px}
.event-more{font-size:14px;color:var(--red);margin-top:6px}

/* newsletter */
.newsletter{position:absolute;left:0;top:2195px;width:1200px;height:101px;background:var(--yellow)}
.newsletter-label{position:absolute;left:203px;top:32px;font-size:25px}
.newsletter-input{position:absolute;left:442px;top:33px;width:426px;height:41px;border:1px solid #8b7a10;font-size:14px;padding:12px 18px;color:var(--text)}
.newsletter-btn{position:absolute;left:875px;top:33px;width:126px;height:41px;background:var(--red);color:var(--white);font-size:18px;display:flex;align-items:center;justify-content:center}

/* footer */
.footer{position:absolute;left:0;top:2296px;width:1200px;height:469px;background:var(--black);color:#ddd}
.foot-head{position:absolute;top:58px;font-size:22px;color:var(--white);letter-spacing:.3px}
.foot-text{font-size:14px;line-height:28px}
.contact-row{display:flex;gap:10px;font-size:14px;line-height:24px}
.map{position:absolute;left:769px;top:102px;width:283px;height:177px;background:linear-gradient(135deg,#e9e2d2,#d6d0c0 55%,#9fc0df 75%,#8fb6dc)}
.foot-rule{position:absolute;left:133px;top:343px;width:945px;height:1px;background:#333}
.foot-nav{position:absolute;left:133px;top:376px;display:flex;gap:28px;font-size:13px;color:#888}
.copyright{position:absolute;left:133px;top:409px;font-size:12px;color:#666}
</style>
</head>
<body>

<header class="topbar">
  <div class="pill pill-pickup">Order for Pickup</div>
  <div class="pill pill-delivery">Order for Delivery</div>
  <div class="call">
    <div class="call-label">
      <svg width="14" height="14" viewBox="0 0 24 24"><path fill="none" stroke="#fff" stroke-width="2" d="M5 3h4l2 5-3 2a12 12 0 0 0 6 6l2-3 5 2v4a2 2 0 0 1-2 2A18 18 0 0 1 3 5a2 2 0 0 1 2-2z"/></svg>
      CLICK TO CALL
    </div>
    <div class="call-number">773-555-0142</div>
  </div>
</header>

<nav class="mainnav">
  <a>HOME</a><a>ABOUT</a><a>LOCATION &amp; HOURS</a><a>EVENTS</a><a>BOOKING</a><a>BLOG</a><a>CONTACT US</a>
</nav>

<section class="hero">
  <div class="hero-bg" role="img" aria-label="Dark wooden plank background"></div>
  <div class="brand"><span class="brand-dot"></span><span class="brand-name">Millbrook Cafe</span></div>
  <div class="arrow arrow-prev"><svg width="16" height="16" viewBox="0 0 16 16"><path d="M10 3L5 8l5 5" fill="none" stroke="#fff" stroke-width="2.5"/></svg></div>
  <div class="arrow arrow-next"><svg width="16" height="16" viewBox="0 0 16 16"><path d="M6 3l5 5-5 5" fill="none" stroke="#fff" stroke-width="2.5"/></svg></div>
  <div class="hero-kicker">Welcome to the Millbrook Cafe</div>
  <div class="hero-title">Good Wholesome Food for<br>the Mind &amp; Body</div>
  <svg class="abs" style="left:0;top:400px" width="1200" height="200" viewBox="0 0 1200 200">
    <path d="M0 175 C200 80 420 120 600 140 C820 165 1020 120 1200 20 L1200 200 L0 200Z" fill="var(--red)"/>
    <path d="M0 200 C200 105 420 150 600 160 C820 170 1020 140 1200 60 L1200 200Z" fill="var(--white)"/>
  </svg>
</section>

<section>
  <h1 class="welcome-title">Welcome to <span>Millbrook Cafe</span></h1>
  <p class="welcome-text">Fusce ultricies orci ac feugiat suscipit leo massa sodales velit et scelerisque mi tortor at ipsum cligula augue bibendum accumsan vestibulum ut commodo a mi Morbi ornare gravida elit Integer congue augue et malesuada iaculis ipsum dui aliquet felis at cursus magna nisl nec elit Praesent</p>
  <div class="btn-dark">Learn More</div>
</section>

<section class="features" role="img" aria-label="Pink and lilac decorative background">
  <div class="badge badge-menu" role="img" aria-label="Plate of food photo">
    <svg width="80" height="60" viewBox="0 0 80 60"><circle cx="40" cy="8" r="5" fill="none" stroke="#fff" stroke-width="4"/><path d="M8 44a32 32 0 0 1 64 0z" fill="none" stroke="#fff" stroke-width="5"/><rect x="2" y="48" width="76" height="6" rx="3" fill="#fff"/></svg>
    <span style="margin-top:14px">Menu</span><span class="bar"></span>
  </div>
  <div class="badge badge-music" role="img" aria-label="Guitarist on stage photo">
    <svg width="70" height="64" viewBox="0 0 70 64"><path d="M22 50V10l40-8v40" fill="none" stroke="#fff" stroke-width="5"/><ellipse cx="14" cy="52" rx="11" ry="8" fill="#fff"/><ellipse cx="54" cy="44" rx="11" ry="8" fill="#fff"/></svg>
    <span style="margin-top:14px">Music</span><span class="bar"></span>
  </div>
  <div class="badge badge-farm" role="img" aria-label="Farm field at dusk photo">
    <svg width="62" height="68" viewBox="0 0 62 68"><path d="M4 66V24L31 4l27 20v42z" fill="none" stroke="#fff" stroke-width="4"/><rect x="17" y="36" width="28" height="28" fill="none" stroke="#fff" stroke-width="4"/><path d="M17 36l28 28M45 36L17 64" stroke="#fff" stroke-width="3"/></svg>
    <span style="margin-top:14px">Farm</span><span class="bar"></span>
  </div>
</section>

<section>
  <h2 class="events-title">Our Events</h2>
  <article class="event" style="left:118px">
    <div class="event-photo" role="img" aria-label="Glasses of red wine raised in a toast" style="background:linear-gradient(135deg,#7a2a2a,#c77a6a 50%,#4a1a18)"></div>
    <h3 class="event-name">Event Tittle here</h3><div class="event-rule"></div>
    <p class="event-text">sociosqu ad litora torquent per conubia nostra per inceptos hymenaeos Proin nulla arcu nonummy luctus dictum eget</p>
    <div class="event-more">READ MORE</div>
  </article>
  <article class="event" style="left:447px">
    <div class="event-photo" role="img" aria-label="Friends sharing a meal at a dinner table" style="background:linear-gradient(135deg,#5a4030,#c9a58a 50%,#3a2a22)"></div>
    <h3 class="event-name">Event Tittle here</h3><div class="event-rule"></div>
    <p class="event-text">sociosqu ad litora torquent per conubia nostra per inceptos hymenaeos Proin nulla arcu nonummy luctus dictum eget</p>
    <div class="event-more">READ MORE</div>
  </article>
  <article class="event" style="left:776px">
    <div class="event-photo" role="img" aria-label="Overhead view of a table full of dishes" style="background:linear-gradient(135deg,#2e3a40,#7a7a5a 50%,#3a3024)"></div>
    <h3 class="event-name">Event Tittle here</h3><div class="event-rule"></div>
    <p class="event-text">sociosqu ad litora torquent per conubia nostra per inceptos hymenaeos Proin nulla arcu nonummy luctus dictum eget</p>
    <div class="event-more">READ MORE</div>
  </article>
</section>

<section class="newsletter">
  <div class="newsletter-label">Newsletter Sign Up</div>
  <div class="newsletter-input">EMAIL ADDRESS</div>
  <div class="newsletter-btn">Subscribe</div>
</section>

<footer class="footer">
  <h4 class="foot-head" style="left:133px">OUR HOURS</h4>
  <div class="abs foot-text" style="left:133px;top:106px">
    Monday - Friday - 9-3, dinner from 5-10<br>
    Kitchen is closed from 3-5<br>
    Saturday-Sunday - 8-10<br>
    Bar is open 7 days a week, from 5pm - 2am
  </div>

  <h4 class="foot-head" style="left:448px">LOCATIONS</h4>
  <div class="abs" style="left:448px;top:104px">
    <div class="contact-row">
      <svg width="16" height="22" viewBox="0 0 16 22"><path d="M8 1a7 7 0 0 0-7 7c0 5 7 13 7 13s7-8 7-13a7 7 0 0 0-7-7z" fill="var(--yellow)"/><circle cx="8" cy="8" r="2.6" fill="#000"/></svg>
      <div>2150 N. Harlow Avenue<br>Chicago, IL 48213<br>At the Alder avenue stop on the Blue Line</div>
    </div>
    <div class="contact-row">
      <svg width="16" height="18" viewBox="0 0 24 24"><path d="M5 3h4l2 5-3 2a12 12 0 0 0 6 6l2-3 5 2v4a2 2 0 0 1-2 2A18 18 0 0 1 3 5a2 2 0 0 1 2-2z" fill="var(--yellow)"/></svg>
      <div>773-555-0142</div>
    </div>
    <div class="contact-row">
      <svg width="16" height="18" viewBox="0 0 16 12"><rect y="1" width="16" height="11" fill="var(--yellow)"/><path d="M0 1l8 6 8-6" fill="none" stroke="#000" stroke-width="1.3"/></svg>
      <div>info@millbrookcafe.com</div>
    </div>
  </div>

  <h4 class="foot-head" style="left:767px">OUR DIRECTIONS</h4>
  <div class="map" role="img" aria-label="Street map of the Chicago area showing the cafe location"></div>

  <div class="foot-rule"></div>
  <div class="foot-nav"><span>HOME</span><span>ABOUT</span><span>LOCATION &amp; HOURS</span><span>EVENTS</span><span>BOOKING</span><span>BLOG</span><span>CONTACT US</span></div>
  <div class="copyright">© 2017 Company Name &nbsp;All right reserved &nbsp;Term of Use</div>
</footer>

</body>
</html>
```